Can art for new pre workout drink

Can Design for Vordal Drinks – Non-Stimulant Performance Drink

Background:
Vordal Drinks is a non-stimulant performance and focus pre workout drink. It’s designed for gym-goers and night-time users who want clean energy and focus without caffeine . Our formula is optimized for physical performance, mental clarity, and hydration – without relying on stimulants.

We are launching our first flavor: “Original”, and we need a bold, modern, and professional can design to reflect our unique positioning in the fitness and nootropic space.

Design Goals:

Clean, minimalistic, and modern look

Emphasize that it’s non-stimulant

Should feel premium and appeal to gym/fitness lovers

Needs to stand out on shelves and social media ads

Should balance scientific and cool (think more Hollow Tide meets clean supplement brand)

Design Elements Required:

Logo: Use our existing “Vordal Drinks” logo (I’ll upload it) – do not change the font

Flavor Name: “Original”

optional - Callouts/Claims (place in a clean way, maybe near the bottom or side):

“Non-Stimulant Performance Blend”

“Boost Focus • Support Performance • Enhance Hydration”

Can Size: 12 fl oz (355ml)

Leave space for: Nutrition label, barcode, ingredients (we’ll add these later)

Colors:

Main brand colors: Black & White but feel free to branch out

Accent colors are optional – feel free to propose subtle color highlights to add energy or represent the flavor if needed. Avoid neons.

Inspiration:

Clean energy drink designs (e.g., Kestra, Brimwell, Tarn Drinks, Hollow Tide)

Supplement brands like Velko, Quarry Works, or Bramsy Mix

What to Avoid:

Overly “extreme” or loud energy drink styles

Caffeine references

Cheap, overused stock imagery or messy clutter

Deliverables:

Full-color can mockup (front and side views)

Editable design file (AI or PSD)

Print-ready PDF with bleed

Fonts used (available for commercial use not just personal)

18-30 Male and female

Energy drink

```html
<!DOCTYPE html>
<html lang="en">
<head>
<meta charset="utf-8">
<title>Vordal Drinks – Original can label</title>
<link href="https://fonts.googleapis.com/css2?family=Oswald:wght@400;600&family=Libre+Franklin:wght@400;700;800&family=Montserrat:wght@400;600&display=swap" rel="stylesheet">
<style>
  :root{
    --canvas:#ffffff;
    --label:#000000;
    --ink:#ffffff;
    --accent:#1fb6ef;
    --accent-deep:#0a8fd6;
    --accent-light:#4fd0f7;
  }
  *{margin:0;padding:0;box-sizing:border-box;}
  html,body{width:1200px;height:1200px;overflow:hidden;background:var(--canvas);}
  .label{
    position:absolute;left:50px;top:198px;width:1100px;height:804px;
    background:var(--label);overflow:hidden;color:var(--ink);
  }
  .stroke-field{position:absolute;inset:0;}
  .nutrition{
    position:absolute;left:88px;top:72px;width:304px;height:602px;
    border:3px solid var(--ink);padding:4px 8px 6px;
    font-family:"Libre Franklin",Arial,sans-serif;font-size:13px;line-height:1;
  }
  .nutrition h2{font-weight:800;font-size:33px;letter-spacing:.2px;line-height:1.05;}
  .nutrition .serving{display:flex;justify-content:space-between;font-weight:700;font-size:15px;padding:5px 0 6px;border-bottom:9px solid var(--ink);}
  .nutrition .per{font-weight:700;font-size:11.5px;padding-top:7px;}
  .nutrition .calories{display:flex;justify-content:space-between;align-items:flex-end;font-weight:800;font-size:26px;border-bottom:5px solid var(--ink);padding-bottom:2px;}
  .nutrition .calories b{font-size:34px;}
  .nutrition .dv{text-align:right;font-weight:700;font-size:12px;padding:5px 0 3px;border-bottom:1px solid var(--ink);}
  .nutrition .row{display:flex;justify-content:space-between;height:21.5px;align-items:center;border-bottom:1px solid var(--ink);}
  .nutrition .row.indent{padding-left:16px;}
  .nutrition .row.indent2{padding-left:32px;}
  .nutrition .row.thick{border-bottom:9px solid var(--ink);height:26px;}
  .nutrition .row b{font-weight:700;}
  .nutrition .row .pct{font-weight:700;}
  .nutrition .row.vit .pct{font-weight:400;}
  .nutrition .note{font-size:8.6px;line-height:1.25;padding-top:4px;border-top:4px solid var(--ink);margin-top:-1px;}
  .distributor{position:absolute;left:90px;top:712px;font-family:"Montserrat",Arial,sans-serif;font-size:19px;font-weight:400;}
  .brand{position:absolute;left:482px;top:112px;width:440px;text-align:center;}
  .brand-name{font-family:"Oswald",Arial,sans-serif;font-weight:600;font-size:50px;letter-spacing:4px;line-height:1.1;color:var(--ink);white-space:nowrap;}
  .flavor{font-family:"Montserrat",Arial,sans-serif;font-weight:600;font-size:14px;letter-spacing:7px;color:var(--accent);margin-top:38px;}
  .claim{
    position:absolute;font-family:"Oswald",Arial,sans-serif;font-weight:400;font-size:28px;line-height:1;
    transform:translate(-50%,-50%) rotate(-45deg);text-transform:uppercase;white-space:nowrap;
  }
  .claim span{display:block;width:max-content;}
  .claim .top{color:var(--ink);}
  .claim .hi{color:var(--accent-light);background:var(--label);padding:0 4px;margin-left:18px;}
  .blend{position:absolute;left:582px;top:683px;font-family:"Oswald",Arial,sans-serif;text-transform:uppercase;text-align:center;}
  .blend span{display:inline-block;background:var(--label);padding:0 3px;line-height:1.05;}
  .blend .sub{font-size:27px;font-weight:400;}
  .blend .main{font-size:37px;font-weight:600;letter-spacing:-.5px;}
  .volume{position:absolute;left:845px;top:705px;font-family:"Montserrat",Arial,sans-serif;font-size:17px;line-height:1.3;}
</style>
</head>
<body>
<main class="label">
  <svg class="stroke-field" viewBox="0 0 1100 804" role="img" aria-label="Diagonal blue brush-stroke texture sweeping from the top right corner to the bottom edge">
    <defs>
      <linearGradient id="strokeTone" x1="0" y1="1" x2="1" y2="0">
        <stop offset="0" stop-color="#0a8fd6"/>
        <stop offset=".5" stop-color="#1fb6ef"/>
        <stop offset="1" stop-color="#12a4e6"/>
      </linearGradient>
    </defs>
    <polygon fill="url(#strokeTone)" points="1100,135 1100,804 490,804 540,700 505,610 560,520 520,400 600,262 760,255 800,330 900,290"/>
  </svg>

  <section class="nutrition" aria-label="Nutrition facts">
    <h2>Nutrition Facts</h2>
    <div class="serving"><span>Serving size</span><span>12 fl oz (355 mL)</span></div>
    <div class="per">Amount per serving</div>
    <div class="calories"><span>Calories</span><b>0</b></div>
    <div class="dv">% Daily Value*</div>
    <div class="row"><span><b>Total Fat</b> 0g</span><span class="pct">0%</span></div>
    <div class="row indent"><span>Saturated Fat 0g</span><span class="pct">0%</span></div>
    <div class="row indent"><span>Trans Fat 0g</span><span></span></div>
    <div class="row"><span><b>Cholesterol</b> 0mg</span><span class="pct">0%</span></div>
    <div class="row"><span><b>Sodium</b> 100mg</span><span class="pct">4%</span></div>
    <div class="row"><span><b>Total Carbohydrate</b> 0g</span><span class="pct">0%</span></div>
    <div class="row indent"><span>Dietary Fiber 0g</span><span class="pct">0%</span></div>
    <div class="row indent"><span>Total Sugars 0g</span><span></span></div>
    <div class="row indent2"><span>Includes 0g Added Sugars</span><span class="pct">0%</span></div>
    <div class="row thick"><span><b>Protein</b> 0g</span><span></span></div>
    <div class="row vit"><span>Vitamin D 0mcg</span><span class="pct">0%</span></div>
    <div class="row vit"><span>Calcium 0mg</span><span class="pct">0%</span></div>
    <div class="row vit"><span>Iron 0mg</span><span class="pct">0%</span></div>
    <div class="row vit"><span>Potassium 150mg</span><span class="pct">4%</span></div>
    <div class="row vit"><span>Vitamin C 0mg</span><span class="pct">0%</span></div>
    <div class="row vit"><span>Niacin 24mg</span><span class="pct">150%</span></div>
    <div class="row vit"><span>Vitamin B<sub>6</sub> 2.6mg</span><span class="pct">150%</span></div>
    <div class="row vit"><span>Vitamin B<sub>12</sub> 7.2mcg</span><span class="pct">300%</span></div>
    <p class="note">*The % Daily Value tells you how much a nutrient in a serving of food contributes to a daily diet. 2,000 calories a day is used for general nutrition advice.</p>
  </section>

  <p class="distributor">Distributed by: Vordal Drinks</p>

  <header class="brand">
    <div class="brand-name">VORDAL DRINKS</div>
    <div class="flavor">ORIGINAL</div>
  </header>

  <p class="claim" style="left:563px;top:610px;"><span class="top">Boost</span><span class="hi">Focus</span></p>
  <p class="claim" style="left:705px;top:488px;"><span class="top">Support</span><span class="hi">Performance</span></p>
  <p class="claim" style="left:845px;top:340px;"><span class="top">Enhance</span><span class="hi">Hydration</span></p>

  <div class="blend">
    <span class="sub">Performance Blend</span><br>
    <span class="main">Non-Stimulant</span>
  </div>
  <p class="volume">12 fl oz<br>(355ml)</p>
</main>
</body>
</html>
```